Business Card Design Project

Use our current logo. Clean design.

Industry/Entity Type

Business

Requirements
Must have
• Marisela DUBRANCQ
M. Law
Managing Partner

Alpenvorsa AG
Kornhalmweg 214
CH-3097 Liebefeld

M. +41 79 412 56 27
T. +41 31 928 44 10
F. +41 31 928 44 19

m.dubrancq@alpenvorsa-example.com
www.alpenvorsa-example.com

```html
<!DOCTYPE html>
<html lang="en">
<head>
<meta charset="utf-8">
<title>Alpenvorsa AG – Business Card</title>
<link rel="stylesheet" href="https://fonts.googleapis.com/css2?family=Lato:wght@400;700&display=swap">
<style>
  :root {
    --page-bg: #ffffff;
    --card-edge: #ffffff;
    --card-face: #e9e9e9;
    --band-blue: #1c1ce0;
    --ink: #1a1a1a;
    --detail-ink: #555555;
  }
  * { margin: 0; padding: 0; box-sizing: border-box; }
  html, body {
    width: 1002px;
    height: 1200px;
    overflow: hidden;
    background: var(--page-bg);
    font-family: "Lato", sans-serif;
  }
  .canvas {
    position: relative;
    width: 1002px;
    height: 1200px;
    display: flex;
    align-items: center;
    justify-content: center;
  }
  .business-card {
    position: relative;
    width: 900px;
    height: 560px;
    background: var(--card-edge);
    border-radius: 22px;
    box-shadow: 0 0 0 1px #dcdcdc;
    padding: 14px;
  }
  .card-face {
    position: relative;
    width: 100%;
    height: 100%;
    background: var(--card-face);
    border-radius: 14px;
  }
  .band {
    position: absolute;
    left: 8px;
    right: 8px;
    height: 22px;
    background: var(--band-blue);
    border-radius: 11px;
  }
  .band--top { top: 40px; }
  .band--bottom { bottom: 32px; }

  .contact-details {
    position: absolute;
    left: 56px;
    top: 92px;
    width: 340px;
    color: var(--detail-ink);
    font-size: 15px;
    line-height: 21px;
  }
  .contact-group + .contact-group { margin-top: 12px; }
  .person-name {
    font-size: 17px;
    font-weight: 700;
    color: var(--ink);
  }

  .brand {
    position: absolute;
    left: 420px;
    top: 190px;
    width: 400px;
    text-align: center;
    color: var(--ink);
  }
  .brand-name {
    font-size: 52px;
    font-weight: 400;
    letter-spacing: 1px;
    line-height: 1;
  }
  .brand-line {
    margin-top: 14px;
    font-size: 15px;
    font-weight: 400;
    letter-spacing: 3px;
    text-transform: uppercase;
  }
</style>
</head>
<body>
  <main class="canvas">
    <section class="business-card" aria-label="Alpenvorsa AG business card">
      <div class="card-face">
        <div class="band band--top"></div>

        <address class="contact-details" style="font-style: normal;">
          <div class="contact-group">
            <p class="person-name">Marisela DUBRANCQ</p>
            <p>M. Law</p>
            <p>Managing Partner</p>
          </div>
          <div class="contact-group">
            <p>Alpenvorsa AG</p>
            <p>Kornhalmweg 214</p>
            <p>CH-3097 Liebefeld</p>
          </div>
          <div class="contact-group">
            <p>M. +41 79 412 56 27</p>
            <p>T. +41 31 928 44 10</p>
            <p>F. +41 31 928 44 19</p>
          </div>
          <div class="contact-group">
            <p>m.dubrancq@alpenvorsa-example.com</p>
            <p>www.alpenvorsa-example.com</p>
          </div>
        </address>

        <div class="brand">
          <p class="brand-name">Alpenvorsa</p>
          <p class="brand-line">Alpenvorsa AG</p>
        </div>

        <div class="band band--bottom"></div>
      </div>
    </section>
  </main>
</body>
</html>
```